Social Media Marketing Website

I would like someone to finish off my website as the previous designer has decided otherwise. I like the current layout but it can be better. I also want the site to reflect my portfolio uploaded on each brand I have worked with. I need to upload videos and make the website responsive and load very quickly. It also needs to be mobile and tablet friendly. I know my way around websites and what is current. my website is www.pkdnorthly.com

Target Market(s)

Business seeking brand consultation and ecommerce solutions

Industry/Entity Type

Digital Marketing

Coding

Coded - Design and coding required

Number of Pages Required

5+ page

Font styles to use
Other font styles liked:
• Bebas Neue

Colors
ffffff
aaaaaa
f5f5f5
fffbf0

Requirements
Must have
• Fast loading website that is easy to navigate. Can withstand video content and high res pictures. Easy backend to operate. Google Analytics Set Up.
Nice to have
• Interactive site
Should not have
• Complex design that is not easy to navigate for the non tech savvy visitor.

```html
<!DOCTYPE html>
<html lang="en">
<head>
<meta charset="utf-8">
<title>Pelham Kerr Dunmore – Social Media Marketing</title>
<link rel="stylesheet" href="https://fonts.googleapis.com/css2?family=Oswald:wght@500&family=Open+Sans:wght@400;600;700&display=swap">
<style>
:root{
  --white:#ffffff;
  --ink:#1f2733;
  --text:#555b63;
  --muted:#aaaaaa;
  --line:#d6d6d6;
  --tile-line:#e2e2e2;
  --navy:#283240;
  --navy-deep:#222b37;
  --gold:#e2b62a;
}
*{box-sizing:border-box;margin:0;padding:0}
html,body{width:1200px;height:3422px;overflow:hidden;background:var(--white)}
body{position:relative;font-family:"Open Sans",Arial,sans-serif;color:var(--text)}
.abs{position:absolute}
.heading{font-family:"Oswald",Impact,sans-serif;font-weight:500;color:var(--ink);text-transform:uppercase;text-align:center;width:1200px;left:0;line-height:1.2}

/* hero */
.hero{position:absolute;left:0;top:0;width:1200px;height:618px;background:linear-gradient(160deg,#5b4c40 0%,#3e352e 45%,#2e2824 100%)}
.hero-photo{position:absolute;inset:0;background:radial-gradient(ellipse at 30% 80%,rgba(190,180,165,.35),transparent 60%),radial-gradient(ellipse at 75% 70%,rgba(170,160,150,.3),transparent 55%)}
.logo{position:absolute;left:100px;top:18px;width:120px;height:120px;border:3px solid var(--white);display:flex;align-items:center;justify-content:center;text-align:center;color:var(--white);font-size:17px;line-height:20px;font-weight:400}
.nav{position:absolute;top:50px;right:100px;display:flex;gap:30px;align-items:center}
.nav a{color:var(--white);text-decoration:none;font-family:"Oswald",sans-serif;font-weight:500;font-size:16px;letter-spacing:.3px}
.hero-title{position:absolute;top:200px;left:0;width:1200px;text-align:center;color:var(--white);font-family:"Oswald",sans-serif;font-weight:500;font-size:70px;line-height:96px}
.hero-sub{position:absolute;top:300px;left:0;width:1200px;text-align:center;color:var(--white);font-size:28px;font-weight:600;line-height:40px}
.btn-outline{position:absolute;left:506px;top:367px;width:187px;height:53px;border:2px solid var(--white);color:var(--white);font-family:"Oswald",sans-serif;font-size:17px;display:flex;align-items:center;justify-content:center}

.intro{position:absolute;top:808px;left:220px;width:760px;text-align:center;font-size:14px;line-height:30px}

/* case studies */
.case-photo{position:absolute;background:linear-gradient(135deg,#e8e6e2,#c9c6c0 60%,#a9a39a)}
.case-card{position:absolute;background:var(--white);border:2px solid var(--line);padding:40px 44px}
.case-card h4{font-size:20px;font-weight:600;color:var(--ink);margin:20px 0 12px;line-height:28px}
.case-card p{font-size:14px;line-height:25px}
.btn-dark{display:inline-flex;align-items:center;justify-content:center;width:130px;height:46px;background:var(--navy);color:var(--white);font-weight:700;font-size:14px}
.client-name{font-size:48px;font-weight:600;color:var(--gold);line-height:56px}
.client-brand{display:flex;align-items:center;gap:16px;font-size:36px;font-weight:600;color:var(--ink);line-height:60px}
.client-brand .mark{width:60px;height:60px;background:var(--ink);border-radius:50%;flex:none}

/* brands */
.brands{position:absolute;top:2361px;left:98px;display:grid;grid-template-columns:repeat(4,237px);column-gap:18px;row-gap:24px}
.brand-tile{height:96px;border:2px solid var(--tile-line);display:flex;align-items:center;justify-content:center;color:var(--muted);font-size:24px;font-weight:600;white-space:nowrap}

/* contact */
.contact{position:absolute;left:0;top:2815px;width:1200px;height:607px;background:linear-gradient(135deg,var(--navy),var(--navy-deep))}
.contact .heading{color:var(--white);top:58px;font-size:58px}
.label{position:absolute;color:var(--white);font-size:11px;font-weight:600}
.section-label{position:absolute;color:var(--white);font-size:14px;font-weight:700}
.field{position:absolute;background:var(--white)}
.btn-submit{position:absolute;left:646px;top:454px;width:84px;height:32px;border:2px solid var(--white);color:var(--white);font-size:13px;font-weight:700;display:flex;align-items:center;justify-content:center}
.info-row{position:absolute;left:810px;display:flex;align-items:center;gap:22px;color:var(--white);font-size:13px;line-height:24px}
.info-icon{width:38px;height:38px;border:2px solid var(--white);border-radius:50%;display:flex;align-items:center;justify-content:center;flex:none}
.socials{position:absolute;left:810px;top:430px;display:flex;gap:14px}
.socials span{width:28px;height:28px;background:var(--white);border-radius:4px}
.divider{position:absolute;left:98px;top:522px;width:1004px;height:1px;background:rgba(255,255,255,.2)}
.copyright{position:absolute;top:549px;left:0;width:1200px;text-align:center;color:var(--white);font-size:13px}
</style>
</head>
<body>

<header class="hero">
  <div class="hero-photo" role="img" aria-label="Photo of a team working around a table with documents and charts"></div>
  <div class="logo">Pelham<br>Kerr<br>Dunmore</div>
  <nav class="nav">
    <a>WORK</a><a>SERVICES</a><a>ABOUT</a><a>BLOG</a><a>CONTACT</a>
    <svg width="18" height="18" viewBox="0 0 18 18"><circle cx="7.5" cy="7.5" r="5.5" fill="none" stroke="#fff" stroke-width="2.5"/><line x1="11.5" y1="11.5" x2="16.5" y2="16.5" stroke="#fff" stroke-width="2.5"/></svg>
  </nav>
  <h1 class="hero-title">PELHAM KERR DUNMORE</h1>
  <p class="hero-sub">We are a social media marketing company</p>
  <div class="btn-outline">GET MORE INFO</div>
</header>

<h2 class="heading abs" style="top:708px;font-size:58px">Our Work</h2>
<p class="intro">Lorem ipsum dolor sit amet, consectetur adipiscing elit, sed do eiusmod tempor incididunt ut labore et dolore magna aliq&nbsp; minim veniam, quis nostrud exercitationratione volu ullamco laboris nisi ut aliquip</p>

<div class="case-photo" style="left:0;top:942px;width:548px;height:570px" role="img" aria-label="Desktop computer on a wooden desk showing a finance report dashboard"></div>
<article class="case-card" style="left:513px;top:985px;width:584px;height:486px">
  <div class="client-name">TOM HARLOW</div>
  <h4>The Problem</h4>
  <p>Professional Boxer Tom Harlow approached Pelham Kerr Dunmore to launch his personal-brand. Tom Harlow signed as a professional to Ironhall Boxing &amp; Promoter Glen Maddox.</p>
  <h4>The Solution</h4>
  <p>PKD launched Tom Harlow to the nation with a strategic plan first unveiling him to his home town at Ashford Rovers FC as a match day sponsor.</p>
  <div class="btn-dark" style="margin-top:24px">READ MORE</div>
</article>

<div class="case-photo" style="left:652px;top:1572px;width:548px;height:572px;background:linear-gradient(135deg,#d8dde2,#9aa3ab 55%,#4b525a)" role="img" aria-label="Computer screen showing a marketing strategy presentation"></div>
<article class="case-card" style="left:98px;top:1613px;width:554px;height:486px">
  <div class="client-brand"><span class="mark"></span>Vale Meridian</div>
  <h4 style="margin-top:24px">The Challenge</h4>
  <p>Pelham Kerr Dunmore were challenged with rebuilding and improving the Vale Meridian Brand. As ever, we approached the task with creativity and inventive functionality and in so doing PKD raised the Vale Meridian brand profile.</p>
  <p style="margin-top:20px">We built a new fully functional website using innovative technology with a user-friendly back end for staff to upload the latest updates and jobs. The new site was designed to work across all devices..</p>
  <div class="btn-dark" style="margin-top:26px">READ MORE</div>
</article>

<h2 class="heading abs" style="top:2225px;font-size:58px">Our Brands</h2>
<div class="brands">
  <div class="brand-tile">Brisk</div>
  <div class="brand-tile">Brisk Sport</div>
  <div class="brand-tile">Brisk Group</div>
  <div class="brand-tile">Brisk Motors</div>
  <div class="brand-tile">Brisk Build</div>
  <div class="brand-tile">Brisk Media</div>
  <div class="brand-tile">Brisk Advance</div>
  <div class="brand-tile">Brisk Freight</div>
  <div class="brand-tile">Brisk Kto</div>
  <div class="brand-tile">Brisk KL</div>
  <div class="brand-tile">Brisk Moto</div>
  <div class="brand-tile">Brisk Racking</div>
</div>

<footer class="contact">
  <h2 class="heading abs">Contact Us</h2>
  <div class="section-label" style="left:98px;top:156px">CONTACT FORM</div>
  <div class="label" style="left:98px;top:200px">NAME :</div>
  <div class="label" style="left:418px;top:200px">PHONE NO :</div>
  <div class="field" style="left:98px;top:224px;width:312px;height:32px"></div>
  <div class="field" style="left:418px;top:224px;width:312px;height:32px"></div>
  <div class="label" style="left:98px;top:268px">EMAIL :</div>
  <div class="field" style="left:98px;top:292px;width:632px;height:32px"></div>
  <div class="label" style="left:98px;top:334px">MESSAGE :</div>
  <div class="field" style="left:98px;top:358px;width:632px;height:80px"></div>
  <div class="btn-submit">SUBMIT</div>

  <div class="section-label" style="left:810px;top:156px">CONTACT INFORMATION</div>
  <div class="info-row" style="top:196px">
    <span class="info-icon"><svg width="14" height="18" viewBox="0 0 14 18"><path d="M7 1a6 6 0 0 0-6 6c0 4.5 6 10 6 10s6-5.5 6-10a6 6 0 0 0-6-6z" fill="none" stroke="#fff" stroke-width="1.8"/><circle cx="7" cy="7" r="2" fill="#fff"/></svg></span>
    <span>We are located at 12 Orchard Lane<br>Kyneton, Victoria</span>
  </div>
  <div class="info-row" style="top:264px">
    <span class="info-icon"><svg width="16" height="16" viewBox="0 0 16 16"><path d="M3 1l3 3-1.5 2.2a9 9 0 0 0 5.3 5.3L12 10l3 3-2 2C6 15 1 10 1 3z" fill="#fff"/></svg></span>
    <span>1 800 555 0199</span>
  </div>
  <div class="info-row" style="top:321px">
    <span class="info-icon"><svg width="16" height="12" viewBox="0 0 16 12"><rect x="0.5" y="0.5" width="15" height="11" fill="#fff"/><path d="M1 1l7 6 7-6" fill="none" stroke="#283240" stroke-width="1.5"/></svg></span>
    <span>info@pkddigital.com</span>
  </div>
  <div class="section-label" style="left:810px;top:392px">SOCIAL</div>
  <div class="socials"><span></span><span></span><span></span><span></span></div>

  <div class="divider"></div>
  <p class="copyright">Copyrights © 2018, PKD Digital. All Rights Reserved.</p>
</footer>

</body>
</html>
```